Business Card Project

We are a small consulting firm. You can experiment with any design.
Must have:
1) Company name - TOLVIN International
2) Company slogan - simple solutions for complex problems
3) Name/Title/Phone/Email/WWW/ - use anything you like as an example.

Industry/Entity Type

Business

```html
<!DOCTYPE html>
<html lang="en">
<head>
<meta charset="utf-8">
<title>TOLVIN International – Business Card</title>
<link rel="stylesheet" href="https://fonts.googleapis.com/css2?family=Exo+2:ital,wght@0,300;0,400;1,300&display=swap">
<style>
  :root {
    --page-bg: #d9d9d9;
    --card-blue: #1f86d4;
    --card-white: #f4f4f4;
    --accent-line: #3aa6ea;
    --ink-grey: #5b5b5b;
    --ink-white: #ffffff;
    --ink-soft: #dbeefb;
  }
  * { margin: 0; padding: 0; box-sizing: border-box; }
  html, body {
    width: 1200px; height: 900px; overflow: hidden;
    background: var(--page-bg);
    font-family: "Exo 2", sans-serif;
  }
  .card {
    position: absolute;
    width: 640px; height: 366px;
    border-radius: 4px;
    box-shadow: 0 6px 18px rgba(0,0,0,0.25);
    overflow: hidden;
  }

  .brand {
    position: absolute;
    display: flex; align-items: center;
  }
  .brand-dot {
    flex: none;
    border-radius: 50%;
  }
  .brand-name {
    font-weight: 400; letter-spacing: 2px;
    white-space: nowrap;
  }

  /* Back side */
  .card-back {
    left: 400px; top: 60px;
    background: var(--card-blue);
  }
  .card-back .brand {
    left: 70px; top: 136px; gap: 22px;
    color: var(--ink-white);
  }
  .card-back .brand-dot {
    width: 56px; height: 56px;
    background: var(--ink-white);
  }
  .card-back .brand-name { font-size: 36px; }
  .slogan {
    position: absolute; left: 40px; bottom: 34px;
    color: var(--ink-soft);
    font-weight: 300; font-size: 21px; letter-spacing: 1.5px;
  }

  /* Front side */
  .card-front {
    left: 160px; top: 470px;
    background: var(--card-white);
  }
  .card-front .brand {
    left: 48px; top: 64px; gap: 24px;
    color: var(--ink-grey);
  }
  .card-front .brand-dot {
    width: 68px; height: 68px;
    background: var(--card-blue);
  }
  .card-front .brand-name { font-size: 38px; }

  .contact-band {
    position: absolute; left: 0; right: 0; bottom: 0; height: 166px;
    background: var(--card-blue);
    border-top: 4px solid var(--accent-line);
  }
  .person {
    position: absolute; left: 40px; top: 28px;
    color: var(--ink-white);
  }
  .person-name {
    font-weight: 400; font-size: 27px; letter-spacing: 0.5px;
    text-transform: uppercase;
  }
  .person-role, .person-company {
    font-weight: 300; font-style: italic; font-size: 19px;
    margin-top: 4px;
  }
  .person-company { margin-top: 8px; }
  .band-divider {
    position: absolute; left: 318px; top: 22px; bottom: 22px;
    width: 1px; background: rgba(255,255,255,0.55);
  }
  .contact-list {
    position: absolute; left: 348px; top: 22px;
    list-style: none; color: var(--ink-white);
  }
  .contact-list li {
    display: flex; align-items: center; gap: 16px;
    height: 40px; font-size: 19px; font-weight: 400; letter-spacing: 0.5px;
    white-space: nowrap;
  }
  .contact-icon {
    width: 28px; height: 28px; flex: none;
  }
</style>
</head>
<body>

<section class="card card-back" aria-label="Business card, back side">
  <div class="brand">
    <span class="brand-dot"></span>
    <span class="brand-name">TOLVIN International</span>
  </div>
  <p class="slogan">simple solutions for complex problems</p>
</section>

<section class="card card-front" aria-label="Business card, front side">
  <div class="brand">
    <span class="brand-dot"></span>
    <span class="brand-name">TOLVIN International</span>
  </div>

  <div class="contact-band">
    <div class="person">
      <p class="person-name">Lukas Brenner</p>
      <p class="person-role">Web Developer</p>
      <p class="person-company">TOLVIN International</p>
    </div>

    <div class="band-divider"></div>

    <ul class="contact-list">
      <li>
        <svg class="contact-icon" viewBox="0 0 28 28" aria-hidden="true">
          <circle cx="14" cy="14" r="12.5" fill="none" stroke="#fff" stroke-width="1.6"/>
          <path d="M10 8.5c-1 .8-1.5 2-1 3.6 1 3 3.6 5.7 6.7 6.8 1.5.5 2.7 0 3.5-1l-2-2-1.5 1c-1.6-.8-2.8-2-3.6-3.6l1-1.5z" fill="#fff"/>
        </svg>
        <span>+41 79 420 18 56</span>
      </li>
      <li>
        <svg class="contact-icon" viewBox="0 0 28 28" aria-hidden="true">
          <circle cx="14" cy="14" r="12.5" fill="none" stroke="#fff" stroke-width="1.6"/>
          <rect x="7.5" y="9.5" width="13" height="9" fill="#fff"/>
          <path d="M7.5 9.5l6.5 5 6.5-5" fill="none" stroke="#1f86d4" stroke-width="1.2"/>
        </svg>
        <span>lukas@tolvinint.com</span>
      </li>
      <li>
        <svg class="contact-icon" viewBox="0 0 28 28" aria-hidden="true">
          <circle cx="14" cy="14" r="12.5" fill="none" stroke="#fff" stroke-width="1.6"/>
          <circle cx="14" cy="14" r="7" fill="#fff"/>
          <g fill="none" stroke="#1f86d4" stroke-width="0.9">
            <ellipse cx="14" cy="14" rx="3" ry="7"/>
            <line x1="7" y1="14" x2="21" y2="14"/>
            <line x1="8" y1="10.5" x2="20" y2="10.5"/>
            <line x1="8" y1="17.5" x2="20" y2="17.5"/>
          </g>
        </svg>
        <span>www.tolvinint.com</span>
      </li>
    </ul>
  </div>
</section>

</body>
</html>
```